Law Office Business Card

We need a business card design to include the following information:
Name of Firm: Brennick Law Group, P.A.
Address: 4627 Sandlot Ave, Ste 208, West Palm Beach, FL 33409
Phone: 561-555-0148
Fax: 561-555-0193
Website: http://www.tbrennicklaw.example

We Need a place for the Person's name and email address. Please start with the following:
Lorna K. Dwyer, Esq.
lorna@tbrennicklaw.example

```html
<!DOCTYPE html>
<html lang="en">
<head>
<meta charset="utf-8">
<title>Brennick Law Group – Business Card</title>
<link href="https://fonts.googleapis.com/css2?family=Libre+Caslon+Text:ital,wght@0,700;1,700&display=swap" rel="stylesheet">
<style>
  :root {
    --card-bg: #fdfcc9;
    --ink-brown: #8b5f3d;
    --rule-brown: #8b5f3d;
    --label-red: #cc2020;
  }
  html, body {
    margin: 0;
    padding: 0;
    overflow: hidden;
    background: var(--card-bg);
  }
  .card {
    position: relative;
    width: 1200px;
    height: 686px;
    background: var(--card-bg);
    font-family: "Libre Caslon Text", Georgia, serif;
    font-weight: 700;
    color: var(--ink-brown);
    overflow: hidden;
  }
  .line {
    position: absolute;
    margin: 0;
    white-space: nowrap;
    line-height: 1;
  }
  .brand-mark {
    position: absolute;
    left: 51px;
    width: 373px;
    top: 120px;
    display: flex;
    flex-direction: column;
    align-items: center;
    gap: 18px;
  }
  .brand-mark__square {
    width: 34px;
    height: 34px;
    background: var(--ink-brown);
  }
  .brand-mark__name {
    font-size: 36px;
    letter-spacing: 1px;
    text-align: center;
    line-height: 1.15;
    color: var(--ink-brown);
  }
  .rule-horizontal {
    position: absolute;
    left: 51px;
    top: 363px;
    width: 373px;
    height: 3px;
    background: var(--rule-brown);
  }
  .rule-vertical {
    position: absolute;
    left: 497px;
    top: 34px;
    width: 3px;
    height: 622px;
    background: var(--rule-brown);
  }
  .person-name { left: 54px; top: 437px; font-size: 32px; letter-spacing: 0.5px; }
  .person-email { left: 54px; top: 491px; font-size: 24px; }
  .firm-name { left: 536px; top: 112px; font-size: 35px; letter-spacing: 1px; }
  .contact { left: 536px; font-size: 31px; }
  .contact--phone { top: 165px; }
  .contact--fax { top: 217px; }
  .contact--web { top: 273px; font-size: 26px; }
  .contact__label {
    font-style: italic;
    color: var(--label-red);
    font-size: 24px;
    margin-left: 12px;
  }
  .contact--web .contact__label { font-size: 22px; }
  .address { left: 536px; font-size: 33px; letter-spacing: 0.5px; }
  .address--1 { top: 386px; }
  .address--2 { top: 438px; }
  .address--3 { top: 490px; }
  .address--4 { top: 542px; }
</style>
</head>
<body>
  <main class="card">
    <div class="brand-mark">
      <span class="brand-mark__square" aria-hidden="true"></span>
      <span class="brand-mark__name">Brennick Law<br>Group</span>
    </div>

    <div class="rule-horizontal" aria-hidden="true"></div>
    <div class="rule-vertical" aria-hidden="true"></div>

    <p class="line person-name">Lorna K. Dwyer, Esq.</p>
    <p class="line person-email">lorna@tbrennicklaw.example</p>

    <p class="line firm-name">Brennick Law Group, P.A.</p>
    <p class="line contact contact--phone">561-555-0148<span class="contact__label">phone</span></p>
    <p class="line contact contact--fax">561-555-0193<span class="contact__label">fax</span></p>
    <p class="line contact contact--web">http://www.tbrennicklaw.example<span class="contact__label">website</span></p>

    <p class="line address address--1">4627 Sandlot Ave,</p>
    <p class="line address address--2">Ste 208,</p>
    <p class="line address address--3">West Palm Beach,</p>
    <p class="line address address--4">FL 33409</p>
  </main>
</body>
</html>
```